MOLVT Study flyer

I need help designing a flyer for a research study that will include brain imaging in adolescents. The info is in the attached document. The study is called the Marrowby Orchard Lantern Vesper Trail (MOLVT) study. Ideally this would be returned as a document that I can edit in the future as we will have several new recruitment phases (different age groups, etc. I also would love to have a logo designed as part of this project, but I recognize that might be a separate design request.

```html
<!DOCTYPE html>
<html lang="en">
<head>
<meta charset="utf-8">
<title>MOLVT Study Flyer</title>
<link href="https://fonts.googleapis.com/css2?family=Poppins:wght@300;400;500;600;700;800&family=Oswald:wght@500;600&display=swap" rel="stylesheet">
<style>
  :root {
    --navy: #141c4a;
    --green: #3db54a;
    --teal: #2a9ba6;
    --teal-light: #2fa3ad;
    --ink: #1b2040;
    --paper: #ffffff;
    --paper-shade: #e9ebee;
    --stage: #d8d8d8;
  }
  * { box-sizing: border-box; margin: 0; padding: 0; }
  html, body { width: 1200px; height: 2182px; overflow: hidden; }
  body {
    background: var(--stage);
    font-family: "Poppins", sans-serif;
    color: var(--ink);
    position: relative;
  }
  .flyer {
    position: absolute;
    left: 40px;
    top: 297px;
    width: 1120px;
    height: 1587px;
    background: linear-gradient(180deg, var(--paper-shade) 0%, var(--paper) 75%);
    overflow: hidden;
    box-shadow: 0 6px 24px rgba(0,0,0,0.18);
  }
  .hero-bg { position: absolute; left: 0; top: 0; width: 1120px; height: 760px; }
  .headline {
    position: absolute;
    left: 0; top: 88px; width: 100%;
    text-align: center;
    font-weight: 800;
    font-size: 84px;
    line-height: 102px;
    letter-spacing: -1.5px;
    color: var(--green);
    text-transform: uppercase;
  }
  .subhead {
    position: absolute;
    left: 0; top: 304px; width: 100%;
    text-align: center;
    font-weight: 300;
    font-size: 45px;
    line-height: 57px;
    color: var(--teal-light);
    text-transform: uppercase;
  }
  .intro {
    position: absolute;
    left: 170px; top: 442px; width: 780px;
    text-align: center;
    font-size: 20.5px;
    line-height: 30px;
    color: #ffffff;
  }
  .illustration-main { position: absolute; left: 0; top: 0; width: 1120px; height: 1587px; pointer-events: none; }
  .section-title {
    position: absolute;
    left: 101px;
    font-weight: 700;
    font-size: 25px;
    color: var(--navy);
    text-transform: uppercase;
    letter-spacing: -0.3px;
  }
  .participation-title { top: 786px; }
  .eligibility-title { top: 1138px; }
  .detail-list {
    position: absolute;
    left: 116px;
    width: 540px;
    list-style: none;
    font-size: 21px;
    line-height: 28.5px;
  }
  .detail-list li { position: relative; padding-left: 23px; margin-bottom: 11px; }
  .detail-list li::before {
    content: ""; position: absolute; left: 2px; top: 12px;
    width: 6px; height: 6px; border-radius: 50%; background: var(--ink);
  }
  .participation-list { top: 830px; width: 520px; }
  .eligibility-list { top: 1180px; }
  .compensation-seal { position: absolute; left: 766px; top: 1109px; width: 224px; height: 224px; }
  .seal-point {
    position: absolute; left: 33px; top: 33px; width: 158px; height: 158px;
    background: var(--green);
  }
  .seal-core {
    position: absolute; left: 20px; top: 20px; width: 184px; height: 184px;
    border-radius: 50%; background: var(--green);
  }
  .seal-text {
    position: absolute; left: 22px; top: 64px; width: 180px;
    text-align: center; color: var(--navy);
    transform: rotate(-6deg);
  }
  .seal-label { font-family: "Oswald", sans-serif; font-weight: 500; font-size: 17px; line-height: 20px; white-space: nowrap; }
  .seal-amount { font-weight: 700; font-size: 56px; line-height: 62px; letter-spacing: -1px; }
  .contact { position: absolute; left: 650px; top: 1370px; }
  .contact-prompt { font-weight: 700; font-size: 26px; line-height: 30px; color: var(--green); }
  .contact-note { margin-top: 38px; font-size: 19px; color: var(--ink); }
  .contact-email { margin-top: 10px; font-weight: 700; font-size: 25px; color: var(--navy); }
  .footer-band { position: absolute; left: 0; width: 100%; }
  .footer-navy { top: 1548px; height: 22px; background: var(--navy); }
  .footer-green { top: 1570px; height: 17px; background: var(--green); }
</style>
</head>
<body>
  <main class="flyer">
    <svg class="hero-bg" viewBox="0 0 1120 760" aria-hidden="true">
      <path fill="var(--navy)" d="M0 0 H1120 V640 C1080 690 1040 705 990 712 L600 740 C520 755 470 760 420 742 C360 720 330 705 280 715 C220 728 170 760 110 748 C70 740 35 720 0 735 Z"/>
    </svg>

    <h1 class="headline">Are you the parent<br>of a child age 10–17?</h1>
    <p class="subhead">Do they worry or overthink<br>negative emotions?</p>
    <p class="intro">Harrowfield University researchers are seeking girls age 10–17 for a study about brain activity in emotions and decision-making and how they relate to puberty, anxiety and depression.</p>

    <svg class="illustration-main" viewBox="0 0 1120 1587">
      <defs>
        <linearGradient id="panelTone" x1="0" y1="0" x2="0" y2="1">
          <stop offset="0" stop-color="#2aa9b2"/>
          <stop offset="1" stop-color="#22929c"/>
        </linearGradient>
        <linearGradient id="studyTone" x1="0" y1="0" x2="1" y2="1">
          <stop offset="0" stop-color="#e8e4f2"/>
          <stop offset="1" stop-color="#f3ece2"/>
        </linearGradient>
      </defs>
      <polygon role="img" aria-label="Illustration of a girl reading a tablet while sitting on a stack of books, with a light bulb, clouds and a potted plant on a teal panel" fill="url(#panelTone)" points="582,610 1022,513 1018,1095 690,1150"/>
      <rect role="img" aria-label="Illustration of a boy reading on a pile of books surrounded by school and science icons" x="160" y="1330" width="390" height="240" rx="30" fill="url(#studyTone)"/>
    </svg>

    <h2 class="section-title participation-title">Study participation involves:</h2>
    <ul class="detail-list participation-list">
      <li>One one-hour interview (online or in-person) where your child will discuss their thoughts</li>
      <li>Online questionnaires (parent and child)</li>
      <li>One two-hour visit where your child will complete an MRI scan, answer questions about their puberty stage, and have a small hair sample taken to study puberty hormones</li>
    </ul>

    <h2 class="section-title eligibility-title">Your child may be eligible if they:</h2>
    <ul class="detail-list eligibility-list">
      <li>Are age 10–17</li>
      <li>Tend to worry or overthink negative thoughts</li>
      <li>have not been diagnosed with psychosis, learning problems, or autism</li>
    </ul>

    <div class="compensation-seal">
      <div class="seal-point" style="transform: rotate(0deg)"></div>
      <div class="seal-point" style="transform: rotate(15deg)"></div>
      <div class="seal-point" style="transform: rotate(30deg)"></div>
      <div class="seal-point" style="transform: rotate(45deg)"></div>
      <div class="seal-point" style="transform: rotate(60deg)"></div>
      <div class="seal-point" style="transform: rotate(75deg)"></div>
      <div class="seal-core"></div>
      <div class="seal-text">
        <div class="seal-label">COMPENSATION UP TO</div>
        <div class="seal-amount">$140</div>
      </div>
    </div>

    <div class="contact">
      <p class="contact-prompt">Interested in participating?<br>Want more information?</p>
      <p class="contact-note">Please contact us!</p>
      <p class="contact-email">molvtstudy@harrowfield.edu</p>
    </div>

    <div class="footer-band footer-navy"></div>
    <div class="footer-band footer-green"></div>
  </main>
</body>
</html>
```